digger and truck hire

this is a new business - Digger and Truck
we would like to include the attached photo of the digger and truck - as the truck is red and the digger is green
maybe either black or white lettering which ever suits

Business

Contact Information for Business Card

RDL - Bodrins 2.5t Mini Digger and 7t Tip Truck -Hire, full attachments, augers, trenching, site preparation, small aggregate deliveries
Phone 0261593847
bodrin.rdl@velmo.co.nz

```html
<!DOCTYPE html>
<html lang="en">
<head>
<meta charset="utf-8">
<title>RDL Business Card</title>
<link rel="stylesheet" href="https://fonts.googleapis.com/css2?family=Quicksand:wght@500;700&display=swap">
<style>
  :root {
    --page-bg: #e9e7e4;
    --card-white: #ffffff;
    --band-black: #050505;
    --ink: #111111;
    --text-light: #ffffff;
    --truck-green: #3f9a2c;
    --truck-dark: #1d1d1d;
    --digger-yellow: #e9b224;
    --digger-dark: #3a3426;
  }
  * { box-sizing: border-box; margin: 0; padding: 0; }
  html, body {
    width: 1200px;
    height: 555px;
    overflow: hidden;
    background: var(--page-bg);
    font-family: "Quicksand", "Arial Rounded MT Bold", sans-serif;
  }
  .card {
    position: absolute;
    left: 180px;
    top: 37px;
    width: 840px;
    height: 480px;
    background: var(--card-white);
    border-radius: 26px;
    overflow: hidden;
    box-shadow: 0 6px 18px rgba(0,0,0,0.18);
  }
  .info-band {
    position: absolute;
    left: 0;
    top: 165px;
    width: 100%;
    height: 245px;
    background: var(--band-black);
  }
  .vehicle-photo {
    position: absolute;
    border-radius: 18px;
  }
  .vehicle-photo--truck {
    left: 70px;
    top: 40px;
    width: 210px;
    height: 150px;
    background: radial-gradient(ellipse at 50% 40%, var(--truck-green) 0%, #2e6e22 45%, var(--truck-dark) 80%);
  }
  .vehicle-photo--digger {
    left: 470px;
    top: 22px;
    width: 330px;
    height: 140px;
    background: linear-gradient(100deg, var(--digger-yellow) 0%, #f1c543 45%, var(--digger-dark) 70%, var(--digger-yellow) 100%);
  }
  .brand-mark {
    position: absolute;
    left: 330px;
    top: 140px;
    width: 132px;
    height: 50px;
    background: var(--card-white);
    border: 3px solid var(--band-black);
    border-radius: 12px;
    display: flex;
    align-items: center;
    justify-content: center;
    font-weight: 700;
    font-size: 32px;
    color: var(--ink);
    letter-spacing: 1px;
  }
  .business-title {
    position: absolute;
    left: 92px;
    top: 210px;
    font-weight: 700;
    font-size: 25px;
    letter-spacing: 0.8px;
    color: var(--text-light);
    white-space: nowrap;
  }
  .contact-list {
    position: absolute;
    left: 488px;
    top: 252px;
    list-style: none;
    color: var(--text-light);
    font-weight: 500;
    font-size: 19px;
    letter-spacing: 0.4px;
  }
  .contact-item {
    display: flex;
    align-items: center;
    gap: 12px;
    height: 36px;
  }
  .contact-icon { width: 16px; height: 16px; flex: none; }
  .person {
    position: absolute;
    left: 112px;
    top: 318px;
    color: var(--text-light);
  }
  .person-name {
    font-weight: 700;
    font-size: 27px;
    letter-spacing: 1px;
  }
  .person-role {
    font-weight: 700;
    font-size: 14px;
    letter-spacing: 0.6px;
    margin-top: 2px;
  }
  .services {
    position: absolute;
    left: 135px;
    top: 414px;
    color: var(--ink);
    font-weight: 700;
    font-size: 18px;
    line-height: 24px;
    letter-spacing: 0.4px;
    white-space: nowrap;
  }
  .services .dot {
    display: inline-block;
    width: 9px;
    height: 9px;
    border-radius: 50%;
    background: var(--ink);
    margin: 0 12px;
    vertical-align: 2px;
  }
</style>
</head>
<body>
  <div class="card">
    <div class="vehicle-photo vehicle-photo--truck" role="img" aria-label="Green monster truck photo"></div>
    <div class="vehicle-photo vehicle-photo--digger" role="img" aria-label="Yellow backhoe digger photo"></div>

    <div class="info-band">
    </div>

    <div class="brand-mark">RDL</div>

    <h1 class="business-title">Bodrins 2.5t Mini Digger and 7t Tip Truck</h1>

    <ul class="contact-list">
      <li class="contact-item">
        <svg class="contact-icon" viewBox="0 0 16 16" aria-hidden="true">
          <rect x="1.5" y="1.5" width="13" height="13" fill="none" stroke="#ffffff" stroke-width="1.6"/>
        </svg>
        <span>0261593847</span>
      </li>
      <li class="contact-item">
        <svg class="contact-icon" viewBox="0 0 16 16" aria-hidden="true">
          <rect x="1" y="3.5" width="14" height="9.5" fill="#ffffff"/>
          <path d="M1 3.5 L8 9 L15 3.5" fill="none" stroke="#050505" stroke-width="1.3"/>
        </svg>
        <span>bodrin.rdl@velmo.co.nz</span>
      </li>
    </ul>

    <div class="person">
      <div class="person-name">BODRIN</div>
      <div class="person-role">DIRECTOR</div>
    </div>

    <p class="services">
      Hire<span class="dot"></span>Full Attachments<span class="dot"></span>Augers<span class="dot"></span>Trenching,<br>
      Site Preparation<span class="dot"></span>Small Aggregate Deliveries
    </p>
  </div>
</body>
</html>
```